FItness Bootcamp Flyer

We need an A4 flyer to distribute on an advertising board, and also distribute in the mail.

It should contain a photo(s) of females exercising and having fun outdoors.

It should contain the following text and if you think it could be worded better please change as I'm just looking at getting people to come along:

- KestrelMove Studio Outdoor Bootcamp
Get moving, get fit and feel great

Commencing 19th May

Get results before the winter season
6 Week Bootcamp for $49. Limited numbers!
Or casual visit $10 per session

Now is the time to:
- Lose Weight and Tone-up
- Build Strength and Endurance
- Increase Cardio Fitness
- Improve Your Energy and Vitality
- Fun Varied and Exciting Training Programs
- ALL Fitness Levels

LADIES ONLY BOOTCAMP SUBIACO
Monday 6:30-7:15am, 8:30-9:15am
Wednesday 6:30-7:!5am, 8:30-9:15am
Friday 8:30-9:15am,

Register you place now on 0428 574 812 or email: kestrelmovestudio@fernmail.net

facebook.com/KestrelMove Studio

Target Market(s)

Females 20-60yrs

Industry/Entity Type

Advertising

Requirements
Nice to have
• - We like the words and style of the Harbourline Open Air Training flyer attached
- Also the Vanta Group brochure
- I like the colour Blue, Green, Pink. They don't all have to be used but at least one would be nice thank you

```html
<!DOCTYPE html>
<html lang="en">
<head>
<meta charset="utf-8">
<title>KestrelMove Studio Outdoor Bootcamp Flyer</title>
<link rel="stylesheet" href="https://fonts.googleapis.com/css2?family=Source+Sans+3:wght@300;400;600;700&display=swap">
<style>
  :root {
    --page-bg: #1b1b1b;
    --title-blue: #4a90dc;
    --heading-blue: #2a5cc0;
    --band-blue: #3a63c4;
    --badge-blue: #2c5bb8;
    --footer-dark: #1c1c1c;
    --link-blue: #5aa8f0;
    --text-dark: #2b2b2b;
    --white: #ffffff;
  }
  * { margin: 0; padding: 0; box-sizing: border-box; }
  html, body {
    width: 1200px; height: 900px; overflow: hidden;
    background: var(--page-bg);
    font-family: "Source Sans 3", "Myriad Pro", Arial, sans-serif;
  }
  .flyer {
    position: absolute; left: 290px; top: 28px;
    width: 425px; height: 578px;
    transform: scale(1.46); transform-origin: top left;
    background: var(--white); overflow: hidden;
  }
  .flyer > * { position: absolute; }
  .hero-photo {
    left: 0; top: 0; width: 425px; height: 240px;
    background: linear-gradient(180deg, #eef2f6 0%, #dfe6ee 40%, #8f8a86 62%, #55585c 80%, #3f4246 100%);
  }
  .panel-shape { left: 0; top: 0; width: 425px; height: 578px; }
  .side-photo {
    left: 0; top: 215px; width: 190px; height: 240px;
    background: linear-gradient(90deg, rgba(214,222,232,.75) 0%, rgba(236,240,246,.55) 60%, rgba(255,255,255,0) 100%);
  }
  .title { left: 18px; top: 24px; color: var(--title-blue); font-size: 27px; line-height: 30px; }
  .title .brand { display: block; font-weight: 700; }
  .title .sub { display: block; font-weight: 300; }
  .badge { left: 310px; top: 203px; width: 110px; height: 110px; }
  .intro { left: 60px; top: 211px; color: var(--heading-blue); font-size: 16.5px; font-weight: 700; }
  .benefits { left: 62px; top: 240px; list-style: none; color: var(--text-dark); font-size: 14.5px; line-height: 20.6px; }
  .benefits li { display: flex; align-items: center; gap: 6px; }
  .benefits svg { width: 14px; height: 14px; flex: none; }
  .session-heading { left: 62px; top: 366px; color: var(--heading-blue); font-size: 15.5px; font-weight: 700; }
  .schedule { left: 62px; top: 389px; color: #1f1f1f; font-size: 14px; line-height: 20.5px; }
  .offer-band {
    left: 0; top: 455px; width: 425px; height: 73px;
    background: var(--band-blue); border-top: 3px solid #5d86d8;
    color: var(--white); text-align: center; font-size: 17.5px; line-height: 21px; padding-top: 3px;
  }
  .contact-band {
    left: 0; top: 528px; width: 425px; height: 50px;
    background: var(--footer-dark); color: var(--white);
    text-align: center; font-size: 16px; line-height: 20px; padding-top: 4px;
  }
  .contact-band .accent { color: var(--link-blue); }
</style>
</head>
<body>
  <article class="flyer">
    <div class="hero-photo" role="img" aria-label="Photo of a woman in a blue singlet running along an outdoor road with rocky hills behind"></div>

    <svg class="panel-shape" viewBox="0 0 425 578" aria-hidden="true">
      <path d="M0,226 Q190,168 425,206 L425,578 L0,578 Z" fill="#ffffff"/>
      <path d="M0,226 Q190,168 425,206" fill="none" stroke="#3a78d4" stroke-width="5"/>
      <path d="M300,196 Q380,196 425,206 L425,300 Q400,240 300,196 Z" fill="#3a78d4"/>
    </svg>

    <div class="side-photo" role="img" aria-label="Faded photo of a woman lifting light blue dumbbells"></div>

    <h1 class="title"><span class="brand">KestrelMove Studio</span><span class="sub">Outdoor Bootcamp</span></h1>

    <svg class="badge" viewBox="-55 -55 110 110" role="img" aria-label="Commencing 19th May">
      <polygon fill="var(--badge-blue)" points="55,0 46.1,9.2 50.8,21.1 39.1,26.1 38.9,38.9 26.1,39.1 21.1,50.8 9.2,46.1 0,55 -9.2,46.1 -21.1,50.8 -26.1,39.1 -38.9,38.9 -39.1,26.1 -50.8,21.1 -46.1,9.2 -55,0 -46.1,-9.2 -50.8,-21.1 -39.1,-26.1 -38.9,-38.9 -26.1,-39.1 -21.1,-50.8 -9.2,-46.1 0,-55 9.2,-46.1 21.1,-50.8 26.1,-39.1 38.9,-38.9 39.1,-26.1 50.8,-21.1 46.1,-9.2"/>
      <g transform="rotate(-28)" fill="#ffffff" font-family="Source Sans 3, sans-serif" font-size="16" text-anchor="middle">
        <text x="0" y="-3">Commencing</text>
        <text x="0" y="16">19th May</text>
      </g>
    </svg>

    <h2 class="intro">Now is the time to</h2>
    <ul class="benefits">
      <li><svg viewBox="0 0 14 14"><rect x="0.5" y="2.5" width="11" height="11" fill="#fff" stroke="#2a5cc0"/><path d="M2.5,7.5 L5.5,10.5 L13,1.5" fill="none" stroke="#2a5cc0" stroke-width="2.4"/></svg>Lose Weight and Tone-up</li>
      <li><svg viewBox="0 0 14 14"><rect x="0.5" y="2.5" width="11" height="11" fill="#fff" stroke="#2a5cc0"/><path d="M2.5,7.5 L5.5,10.5 L13,1.5" fill="none" stroke="#2a5cc0" stroke-width="2.4"/></svg>Build Strength and Endurance</li>
      <li><svg viewBox="0 0 14 14"><rect x="0.5" y="2.5" width="11" height="11" fill="#fff" stroke="#2a5cc0"/><path d="M2.5,7.5 L5.5,10.5 L13,1.5" fill="none" stroke="#2a5cc0" stroke-width="2.4"/></svg>Increase Cardio Fitness</li>
      <li><svg viewBox="0 0 14 14"><rect x="0.5" y="2.5" width="11" height="11" fill="#fff" stroke="#2a5cc0"/><path d="M2.5,7.5 L5.5,10.5 L13,1.5" fill="none" stroke="#2a5cc0" stroke-width="2.4"/></svg>Improve Your Energy and Vitality</li>
      <li><svg viewBox="0 0 14 14"><rect x="0.5" y="2.5" width="11" height="11" fill="#fff" stroke="#2a5cc0"/><path d="M2.5,7.5 L5.5,10.5 L13,1.5" fill="none" stroke="#2a5cc0" stroke-width="2.4"/></svg>Fun Varied and Exciting Training Programs</li>
      <li><svg viewBox="0 0 14 14"><rect x="0.5" y="2.5" width="11" height="11" fill="#fff" stroke="#2a5cc0"/><path d="M2.5,7.5 L5.5,10.5 L13,1.5" fill="none" stroke="#2a5cc0" stroke-width="2.4"/></svg>ALL Fitness Levels</li>
    </ul>

    <h3 class="session-heading">LADIES ONLY BOOTCAMP SUBIACO</h3>
    <p class="schedule">Monday 6:30-7:15am, 8:30-9:15am<br>Wednesday 6:30-7:15am, 8:30-9:15am<br>Friday 8:30-9:15am</p>

    <div class="offer-band">
      <p>Get results before the winter season</p>
      <p>6 Week Bootcamp for $49. Limited numbers!</p>
      <p>Or casual visit $10 per session</p>
    </div>

    <div class="contact-band">
      <p>Register you place now on</p>
      <p><span class="accent">0428 574 812</span> or email: <span class="accent">kestrelmovestudio@fernmail.net</span></p>
    </div>
  </article>
</body>
</html>
```